Letterhead

We need a professional, compelling letterhead that can be used for print and email stationary. We have the logo and the letterhead styling and colors should blend seamlessly and be complimentary. Looking for something unique and thoughtful.
Updates

Reason: There are good ideas and am requesting changes to some ideas in order to make a final decision. Thank you for for submissions. Also, I have uploaded the ai file. Please use that file. Thank you.

If you cannot see the .ai version of the logo that I have tried to upload, please message me if you want to make changes to your submission or submit new design and I will send that file to you directly. This .ai will need to be used in order to ensure high quality printing. Thank you.

Target Market(s)

Clients. Business partners.

Industry/Entity Type

It Professional

Requirements
Must have
• Our logo incorporated. Also the phrase, or tag line - where business thrives.
Should not have
• Not boring. Not typical. Not too busy.

```html
<!DOCTYPE html>
<html lang="en">
<head>
<meta charset="utf-8">
<title>Veridian Advisory — Letterhead</title>
<link rel="stylesheet" href="https://fonts.googleapis.com/css2?family=Tinos:wght@400;700&display=swap">
<style>
  :root {
    --paper: #ffffff;
    --brand-navy: #1f3a6a;
    --green-deep: #00913d;
    --green-mid: #00a86b;
    --green-pale: #bfe3cf;
    --violet-deep: #2b1869;
    --violet-mid: #8a80b6;
    --violet-pale: #f4f4f7;
    --ink: #1a1a1a;
    --type: "Tinos", "Times New Roman", serif;
  }
  * { margin: 0; padding: 0; box-sizing: border-box; }
  html, body {
    width: 900px; height: 1200px; overflow: hidden; background: var(--paper);
  }
  .sheet {
    position: relative; width: 900px; height: 1200px;
    background: var(--paper); font-family: var(--type); color: var(--ink);
  }
  .sheet-bands { position: absolute; inset: 0; width: 900px; height: 1200px; }

  .brand {
    position: absolute; left: 26px; top: 58px;
    display: flex; align-items: center; gap: 12px;
  }
  .brand-square {
    width: 18px; height: 18px; background: var(--brand-navy); flex: none;
  }
  .brand-name {
    color: var(--brand-navy); font-size: 30px; font-weight: 400;
    line-height: 1; white-space: nowrap; letter-spacing: 0;
  }

  .footer-web {
    position: absolute; left: 10px; top: 1172px;
    color: var(--paper); font-size: 15px; font-weight: 700;
  }
  .footer-contact {
    position: absolute; left: 685px; top: 1142px;
    font-size: 15px; line-height: 15px; color: var(--ink);
  }
  .footer-contact li { list-style: none; display: flex; }
  .footer-contact .label { width: 58px; }
</style>
</head>
<body>
<main class="sheet">
  <svg class="sheet-bands" viewBox="0 0 900 1200" aria-hidden="true">
    <defs>
      <linearGradient id="header-sweep" x1="0" y1="0" x2="1" y2="0">
        <stop offset="0.3" stop-color="#ffffff"/>
        <stop offset="0.47" stop-color="var(--green-pale)"/>
        <stop offset="0.75" stop-color="var(--green-mid)"/>
        <stop offset="1" stop-color="var(--green-deep)"/>
      </linearGradient>
      <linearGradient id="footer-sweep" x1="0" y1="0" x2="1" y2="0">
        <stop offset="0" stop-color="var(--violet-deep)"/>
        <stop offset="0.4" stop-color="var(--violet-mid)"/>
        <stop offset="0.72" stop-color="var(--violet-pale)"/>
        <stop offset="1" stop-color="var(--violet-pale)"/>
      </linearGradient>
    </defs>
    <path class="header-wave" fill="url(#header-sweep)"
      d="M0,0 H900 V162 C820,140 740,112 620,118 C470,126 300,178 0,172 Z"/>
    <path class="footer-wave" fill="url(#footer-sweep)"
      d="M0,1105 C150,1120 300,1134 480,1126 C650,1116 780,1098 900,1100 V1200 H0 Z"/>
  </svg>

  <header class="brand">
    <span class="brand-square" aria-hidden="true"></span>
    <h1 class="brand-name">Veridian Advisory</h1>
  </header>

  <footer>
    <p class="footer-web">Web Add :</p>
    <ul class="footer-contact">
      <li><span class="label">Cell</span><span>:</span></li>
      <li><span class="label">Fax</span><span>:</span></li>
      <li><span class="label">Add</span><span>:</span></li>
    </ul>
  </footer>
</main>
</body>
</html>
```